Heron Ridge Crafted Building Contractor

We are in the business to New Construction homes, remodeling, renovations. We do it all soup to nuts. The design should convey southern charm with modern elegance. Nothing too busy. Some how use one of the included picture. Maybe render an artistic look to the house in the picture. Leave a place for Name, email and phone number.

Industry/Entity Type

Residential Construction

Contact Information for Business Card

Class A Building Contractor, Residential Commercial, Licensed , Insured , Bonded, Name, Email, phone number,

Colors
f37122

Requirements
Nice to have
• Would like to see the picture of house included in the design

```html
<!DOCTYPE html>
<html lang="en">
<head>
<meta charset="utf-8">
<title>Heron Ridge Crafted Building Contractor – Business Card</title>
<link href="https://fonts.googleapis.com/css2?family=Cinzel:wght@400;600&family=Arimo:wght@400;700&display=swap" rel="stylesheet">
<style>
  :root {
    --brand-orange: #f37122;
    --brand-orange-deep: #e8631a;
    --paper: #ffffff;
    --photo-warm: #e9d3bd;
    --photo-cream: #f6ebe0;
    --text-grey: #6d6d6d;
    --canvas: #ffffff;
  }
  * { box-sizing: border-box; margin: 0; padding: 0; }
  html, body {
    width: 889px; height: 1200px; overflow: hidden;
    background: var(--canvas);
  }
  .canvas {
    position: relative; width: 889px; height: 1200px;
    display: flex; align-items: center; justify-content: center;
  }
  .business-card {
    position: relative; width: 780px; height: 500px;
    background: var(--paper);
    box-shadow: 0 6px 22px rgba(0,0,0,0.16);
    overflow: hidden;
  }
  .house-photo {
    position: absolute; left: 0; top: 0; width: 100%; height: 430px;
    background:
      linear-gradient(90deg, rgba(255,255,255,0) 0%, rgba(255,255,255,0) 30%, rgba(255,255,255,0.85) 55%, #fff 75%),
      linear-gradient(180deg, var(--photo-cream) 0%, var(--photo-warm) 45%, #f3e4d4 80%, #fff 100%);
  }
  .name-band {
    position: absolute; left: 0; top: 135px; width: 292px; height: 44px;
    background: rgba(255,255,255,0.92);
    box-shadow: 0 2px 6px rgba(0,0,0,0.10);
    display: flex; align-items: center; padding-left: 54px;
  }
  .person-name {
    font-family: "Cinzel", serif; font-size: 20px; letter-spacing: 1px;
    color: var(--brand-orange);
  }
  .brand-block { position: absolute; left: 322px; top: 66px; }
  .brand-name {
    font-family: "Cinzel", serif; font-weight: 400; font-size: 50px;
    letter-spacing: 1px; color: var(--brand-orange); line-height: 1;
  }
  .brand-tagline {
    margin-top: 6px;
    font-family: "Cinzel", serif; font-size: 11.5px; letter-spacing: 1.6px;
    color: var(--brand-orange);
  }
  .contact-block { position: absolute; left: 322px; top: 188px; }
  .service-line {
    font-family: "Arimo", sans-serif; font-weight: 700; font-size: 19px;
    color: var(--brand-orange); margin-bottom: 16px;
  }
  .contact-row {
    display: flex; align-items: center; gap: 10px; margin-bottom: 9px;
    font-family: "Arimo", sans-serif; font-size: 16px; color: var(--text-grey);
  }
  .contact-icon { width: 18px; height: 18px; flex: none; }
  .credentials-band {
    position: absolute; left: 0; bottom: 0; width: 100%; height: 70px;
    background: linear-gradient(180deg, var(--brand-orange) 0%, var(--brand-orange-deep) 100%);
    display: flex; align-items: center; justify-content: center;
    font-family: "Cinzel", serif; font-size: 20px; letter-spacing: 4px; color: #fff;
  }
</style>
</head>
<body>
<main class="canvas">
  <article class="business-card">
    <div class="house-photo" role="img" aria-label="Softly faded photograph of a two-storey southern colonial house with white porch columns"></div>

    <div class="name-band"><span class="person-name">DANIEL R. WHITFIELD</span></div>

    <header class="brand-block">
      <h1 class="brand-name">HERON RIDGE</h1>
      <p class="brand-tagline">CRAFTED BUILDING CONTRACTOR</p>
    </header>

    <section class="contact-block">
      <p class="service-line">Residential Commercial</p>
      <p class="contact-row">
        <svg class="contact-icon" viewBox="0 0 18 18" aria-hidden="true">
          <rect x="1" y="1" width="16" height="16" fill="none" stroke="#f37122" stroke-width="1.5"/>
          <path d="M4 6 L9 10 L14 6" fill="none" stroke="#f37122" stroke-width="1.4"/>
        </svg>
        info@heronridgebuild.com
      </p>
      <p class="contact-row">
        <svg class="contact-icon" viewBox="0 0 18 18" aria-hidden="true">
          <rect x="0" y="0" width="18" height="18" fill="#f37122"/>
          <path d="M5.5 4 L7.5 6.5 L6.5 8 Q8 10.5 10 11.5 L11.5 10.5 L14 12.5 L12.5 14.5 Q7 14 3.5 5.5 Z" fill="#fff"/>
        </svg>
        0123.4567.89
      </p>
    </section>

    <footer class="credentials-band">• LICENSED • INSURED • BONDED •</footer>
  </article>
</main>
</body>
</html>
```